Holistic Psychology clinic flyer-

We need a 3 fold flyer that is both professional and zen looking with holistic elements- bilingual on both sides.
I am looking for a design that conveys the sense of confidence, yet relaxing to the eye and makes people want to pick it up and read it!
We are all about balance (yin, yang) and bringing equilibrium to a person in their quest to get better.

Target Market(s)

families adults, teens children experiencing mental health issues

Industry/Entity Type

Psychologist

Font styles to use
Serif

Colors
fbf289
cee9f5
0455a3

Requirements
Must have
• my logo (spiral) ; French one side; English on the other. Text is provided; Some color but clean, zen elements
• Easy to read text
Nice to have
• nature elements, bamboo? trees etc. sunrise or sunset?
• The sunset back ground provided in the picture is not necessary
• families?
Should not have
• too many distracting elements; not too many colors. colors must be subtle and must flow together

```html
<!DOCTYPE html>
<html lang="en">
<head>
<meta charset="utf-8">
<title>Equilibria – Tri-fold Brochure</title>
<link rel="stylesheet" href="https://fonts.googleapis.com/css2?family=Playfair+Display:wght@400;700&family=Lora:wght@400;700&family=Roboto+Condensed:wght@700&family=Montserrat:wght@500;600&family=Raleway:wght@400&display=swap">
<style>
:root{
  --navy:#1f2158;
  --gold:#dca52c;
  --gold-soft:#f3d27a;
  --sun:#f2e14a;
  --ice:#dff1f9;
  --ice-deep:#bfe3f1;
  --ink:#2b2b33;
  --rule:#c9d3da;
  --stage:#6b6f74;
  --dusk:#2a1c14;
  --amber:#e98d2c;
  --glow:#f7c15f;
}
*{margin:0;padding:0;box-sizing:border-box}
html,body{width:1200px;height:2463px;overflow:hidden}
body{background:var(--stage);position:relative;font-family:"Lora",Georgia,serif;color:var(--ink)}
.spread{position:absolute;left:36px;top:794px;width:1128px;height:875px;display:flex;box-shadow:0 10px 30px rgba(0,0,0,.35)}
.panel{position:relative;width:376px;height:875px;overflow:hidden}

/* services panel */
.services{background:linear-gradient(180deg,#f3f9fc 0%,#eaf5fa 100%);padding:0 27px}
.services .mark{position:absolute;left:166px;top:32px;width:40px;height:40px;border:5px solid var(--gold);border-radius:50%}
.services h2{position:absolute;top:92px;left:0;width:100%;text-align:center;font-family:"Playfair Display",serif;font-weight:400;font-size:22px;color:var(--navy)}
.services .short-rule{position:absolute;top:132px;left:165px;width:46px;height:3px;background:var(--ink)}
.service-list{position:absolute;top:150px;left:27px;right:30px;list-style:none}
.service{padding:12px 0 11px;border-bottom:1px solid var(--rule)}
.service:last-child{border-bottom:none}
.service h3{font-family:"Lora",serif;font-weight:400;font-size:15px;color:var(--navy);margin-bottom:2px}
.service p{font-size:10.4px;line-height:15px;text-align:justify}
.service.gap{padding-top:26px}
.web-button{position:absolute;left:37px;top:810px;width:294px;height:50px;background:var(--gold);border-radius:8px 8px 0 0;color:#fff;font-family:"Montserrat",sans-serif;font-weight:600;font-size:15px;display:flex;align-items:center;justify-content:center}

/* welcome panel */
.welcome{background:linear-gradient(180deg,#ffffff 0%,#f5fbfd 22%,#d8eef7 55%,var(--ice-deep) 100%)}
.welcome .hello{position:absolute;top:40px;width:100%;text-align:center;font-family:"Playfair Display",serif;font-size:21px;color:var(--navy)}
.welcome .brand-name{position:absolute;top:62px;width:100%;text-align:center;font-family:"Playfair Display",serif;font-weight:700;font-size:32px;letter-spacing:1px;color:var(--gold)}
.welcome .intro{position:absolute;top:130px;left:29px;right:30px;font-size:10.4px;line-height:15px;text-align:justify}
.welcome .motto{position:absolute;top:325px;width:100%;text-align:center;font-family:"Playfair Display",serif;font-weight:700;font-size:24px;line-height:30px;color:var(--navy)}
.welcome .bio{position:absolute;top:428px;left:29px;right:30px;font-size:10.4px;line-height:15px;text-align:justify}
.welcome .bio b{font-weight:700}
.swoosh{position:absolute;left:0;top:570px;width:376px;height:140px}
.badge{position:absolute;left:80px;top:565px;width:214px;height:214px;border-radius:50%;background:#fff;border:7px solid var(--gold);display:flex;flex-direction:column;align-items:center;justify-content:center;font-family:"Roboto Condensed",sans-serif;font-weight:700;font-size:13.5px;line-height:19px;color:var(--navy);text-align:center}
.badge .icons{display:flex;gap:4px;margin-bottom:8px}
.badge .icons span{width:20px;height:20px;border-radius:50%;background:var(--navy);display:flex;align-items:center;justify-content:center}
.contact-call{position:absolute;top:796px;width:100%;text-align:center;font-family:"Montserrat",sans-serif;font-weight:600;font-size:15.5px;line-height:20px;color:var(--navy)}
.contact-line{position:absolute;top:842px;width:100%;display:flex;justify-content:center;align-items:center;gap:6px;font-family:"Montserrat",sans-serif;font-weight:500;font-size:14px;color:var(--gold)}
.contact-line .sep{color:var(--navy)}
.contact-line .dot{width:14px;height:14px;border-radius:50%;background:var(--navy);display:inline-flex;align-items:center;justify-content:center}

/* cover panel */
.cover{width:376px;background:#fff}
.cover .scene{position:absolute;inset:0;background:linear-gradient(180deg,#ffffff 0%,#fdf6ec 16%,#f6d9a8 33%,var(--glow) 48%,var(--amber) 62%,#b9561c 76%,#5a2b15 88%,var(--dusk) 100%)}
.logo{position:absolute;top:42px;left:0;width:100%;display:flex;align-items:center;justify-content:center;gap:12px}
.logo .dot{width:34px;height:34px;border-radius:50%;background:var(--sun)}
.logo .name{font-family:"Playfair Display",serif;font-weight:400;font-size:46px;color:var(--navy)}
.cover h1{position:absolute;top:170px;width:100%;text-align:center;font-family:"Playfair Display",serif;font-weight:700;font-size:31px;line-height:40px;color:var(--navy)}
.cover .audience{position:absolute;bottom:14px;width:100%;text-align:center;font-family:"Raleway",sans-serif;font-size:18px;color:#fff}
</style>
</head>
<body>
<main class="spread">

  <section class="panel services">
    <span class="mark"></span>
    <h2>Our Professional Services</h2>
    <span class="short-rule"></span>
    <ul class="service-list">
      <li class="service">
        <h3>Clinical Psychology</h3>
        <p>Psychologists are people specialists. Learn how to better understand both yourself and those in your life. Release some of the emotional and relational distress that drains you. It's time for change!</p>
      </li>
      <li class="service">
        <h3>Integrative Psychotherapy</h3>
        <p>We distill the very best approaches in psychology to help you free your mind, balance your body and heal your spirit. We specialize in helping you understand and harmonize the mind-body connection.</p>
      </li>
      <li class="service">
        <h3>Life Coaching</h3>
        <p>Life's challenges are opportunities for your growth. Our life coaches are skilled, caring and passionate about supporting you. Come in, it's time to discover your potential!</p>
      </li>
      <li class="service gap">
        <h3>Sports Psychology</h3>
        <p>There are many different psychological benefits of sports. Our sports psychologists can work with you to release your mental blocks, improve your performance and ensure success! Dare to aim high!</p>
      </li>
      <li class="service">
        <h3>Psycho-Educational Assessments</h3>
        <p>With the aid of psychometric tests, we can help you to figure out how your mind or that of your child works. We will highlight strengths and give recommendations to remedy any weaknesses. A detailed report and an academic intervention plan is customized for individuals aged 4-64!</p>
      </li>
      <li class="service">
        <h3>Mindfulness Meditation Classes</h3>
        <p>Meditation is much more than a relaxation technique. Mindfulness will bring you a heightened awareness and improved quality of life. These classes are offered weekly and will be useful to you to learn how to meditate and integrate it into your daily life. Find your inner peace!</p>
      </li>
    </ul>
    <div class="web-button">www.equilibriapsy.com</div>
  </section>

  <section class="panel welcome">
    <p class="hello">Welcome to</p>
    <p class="brand-name">EQUILIBRIA</p>
    <p class="intro">We present you with a whole new way of achieving wellness in your life. We offer a variety of clinical and educational services in a professional and peaceful environment. We use an integrative approach. We are delighted to present you with several effective and scientific approaches that can help you. We offer a variety of clinical and educational services in a professional and peaceful environment. We are committed to supporting you in reaching your potential and feeling better by adhering to an integrative mind-body approach. We are passionate about supporting you in reaching your potential and feeling well. It's time to start thinking of you...</p>
    <p class="motto">Calm your mind,<br>Relax your body,<br>Nourish your spirit.</p>
    <p class="bio"><b>Marc Delorme, BSc, MA.</b> is the founder and director of Equilibria. As a clinical psychologist, author and motivational speaker with 26 years of experience, Marc is a pioneer in holistic psychology, an integrative approach that promotes healing and wellness. He and his staff are skilled in using cutting edge mind-body-spirit tools to help you with a variety of health, relational, educational and parenting issues. We look forward to supporting you and your family!</p>
    <svg class="swoosh" viewBox="0 0 376 140" aria-hidden="true">
      <path d="M0 30 C90 110 280 120 376 60 L376 70 C280 132 90 124 0 44 Z" fill="var(--navy)"/>
      <path d="M0 52 C90 128 280 136 376 80" fill="none" stroke="var(--gold-soft)" stroke-width="3"/>
    </svg>
    <div class="badge">
      <div class="icons">
        <span><svg width="10" height="12" viewBox="0 0 10 12"><path d="M5 0a4 4 0 0 1 4 4c0 3-4 8-4 8S1 7 1 4a4 4 0 0 1 4-4z" fill="#fff"/><circle cx="5" cy="4" r="1.5" fill="var(--navy)"/></svg></span>
        <span><svg width="12" height="12" viewBox="0 0 12 12"><circle cx="6" cy="6" r="5" fill="none" stroke="#fff"/><path d="M1 6h10M6 1c-3 3-3 7 0 10M6 1c3 3 3 7 0 10" fill="none" stroke="#fff"/></svg></span>
        <span></span>
      </div>
      4580 Riverside Blvd ,<br>Laval, Québec<br>H7A 2K3<br>www.equilibriapsy.com<br>social:<br>@EquilibriaClinic
    </div>
    <p class="contact-call">CONTACT US TODAY FOR A<br>FREE PHONE CONSULTATION</p>
    <p class="contact-line">
      <span class="dot"><svg width="8" height="8" viewBox="0 0 8 8"><path d="M1 1l2 0 1 2-1 1a5 5 0 0 0 1 1l1-1 2 1 0 2c-4 0-6-2-6-6z" fill="#fff"/></svg></span>
      <span>514-555-0142</span><span class="sep">|</span>
      <span class="dot"><svg width="8" height="6" viewBox="0 0 8 6"><rect x=".5" y=".5" width="7" height="5" fill="none" stroke="#fff"/><path d="M.5.5l3.5 3 3.5-3" fill="none" stroke="#fff"/></svg></span>
      <span>info@equilibriapsy.com</span>
    </p>
  </section>

  <section class="panel cover">
    <div class="scene" role="img" aria-label="Photo: silhouette of a couple leaping joyfully on a lakeshore at golden sunset"></div>
    <div class="logo"><span class="dot"></span><span class="name">Equilibria</span></div>
    <h1>Psychologists<br>and Educational<br>Professionals<br>with an Integrative<br>Approach</h1>
    <p class="audience">Children Teens Adults Couples</p>
  </section>

</main>
</body>
</html>
```